Need to make a work slip for trucking company.

I need a form to fill out for my truck drivers to get signed on delivery. It is for a trucking company and this form will be for each machine equipment move. I have included my old sheet which I need Updated. Its going on a 9.5 inch by 8.5 inch sheet of paper. It should have room for the day, date, customer name, ordered by, P.O. Number, Project Number, Driver, Truck/Trailer, Tolls (needs more room then my old sheet need a few lines under each other for each toll during the machine move), Permits, some room for other information, Loads, Hours, and 2 lines for a Signature and Print Line.
Updates

Need to also include a Pickup Address and a Deliver Address with lines to write in. Also I need to add a Print Line (and labeled Print) for whoever is signing the ticket.

Requirements
Must have
• My new company name and Logo. I have included my new Logo. It must be easy to ready. Must include my company colors. (Concrete Gray, and Neon Blue)

```html
<!DOCTYPE html>
<html lang="en">
<head>
<meta charset="utf-8">
<title>Karven Hauling – Work Slip</title>
<link href="https://fonts.googleapis.com/css2?family=Mulish:wght@400;600;800&display=swap" rel="stylesheet">
<style>
  :root {
    --neon-blue: #146bb5;
    --concrete-gray: #8a8c8e;
    --ink: #2b2b2b;
    --rule: #3a3a3a;
    --ticket-red: #e0312b;
    --paper: #ffffff;
    --frame: #e6e6e6;
  }
  * { margin: 0; padding: 0; box-sizing: border-box; }
  html, body { width: 1200px; height: 1125px; overflow: hidden; background: var(--paper); }
  body { position: relative; font-family: "Mulish", Arial, sans-serif; color: var(--ink); }

  .top-band { position: absolute; left: 0; top: 0; width: 1200px; height: 228px; background: var(--neon-blue); }

  .slip {
    position: absolute; left: 87px; top: 103px; width: 1026px; height: 919px;
    background: var(--paper);
    box-shadow: 0 2px 12px rgba(0,0,0,0.18);
  }
  .slip-frame {
    position: absolute; left: 105px; top: 118px; width: 990px; height: 889px;
    border: 1.5px solid var(--frame);
  }

  .ticket-no { position: absolute; left: 117px; top: 132px; font-size: 20px; color: var(--ticket-red); letter-spacing: 1.5px; }
  .meridiem { position: absolute; left: 988px; top: 132px; font-size: 19px; }

  .brand {
    position: absolute; left: 400px; top: 140px; width: 400px; text-align: center;
    font-size: 40px; font-weight: 800; color: var(--neon-blue); letter-spacing: 1px; line-height: 1;
  }

  .field {
    position: absolute; display: flex; align-items: flex-end;
    height: 30px; font-size: 21px; line-height: 30px; white-space: nowrap;
  }
  .field .line { flex: 1; border-bottom: 1.5px solid var(--rule); margin-left: 10px; height: 24px; }
  .field .line.fixed { flex: none; }

  .rule { position: absolute; height: 0; border-bottom: 1.5px solid var(--rule); }
</style>
</head>
<body>
  <div class="top-band"></div>
  <div class="slip"></div>
  <div class="slip-frame"></div>

  <div class="ticket-no">76890</div>
  <div class="meridiem">A.M / P.M</div>
  <div class="brand">KARVEN HAULING</div>

  <div class="field" style="left:121px; top:203px;">Date :<span class="line fixed" style="width:150px;"></span></div>
  <div class="field" style="left:856px; top:202px; width:221px;">Day &nbsp;:<span class="line"></span></div>

  <div class="field" style="left:121px; top:272px; width:956px;">Customer Name<span class="line" style="margin-left:18px;"></span></div>
  <div class="field" style="left:121px; top:338px; width:956px;">Ordered by<span class="line"></span></div>

  <div class="field" style="left:121px; top:407px; width:465px;">P.O No<span class="line"></span></div>
  <div class="field" style="left:601px; top:407px; width:476px;">Project No<span class="line" style="margin-left:18px;"></span></div>

  <div class="field" style="left:121px; top:477px; width:465px;">Driver<span class="line"></span></div>
  <div class="field" style="left:601px; top:477px; width:476px;">Truck/Trailer<span class="line"></span></div>

  <div class="field" style="left:121px; top:546px; width:465px;">Tolls<span class="line"></span></div>
  <div class="field" style="left:601px; top:546px; width:476px;">Permits<span class="line"></span></div>

  <div class="rule" style="left:172px; top:637px; width:414px;"></div>
  <div class="field" style="left:601px; top:615px; width:476px;">Equipment Type<span class="line"></span></div>

  <div class="field" style="left:121px; top:686px; width:465px;">Pickup Address<span class="line"></span></div>
  <div class="field" style="left:601px; top:686px; width:476px;">Delivery Address<span class="line"></span></div>
  <div class="rule" style="left:285px; top:777px; width:301px;"></div>
  <div class="rule" style="left:777px; top:777px; width:300px;"></div>

  <div class="field" style="left:121px; top:825px;">Loads<span class="line fixed" style="width:247px;"></span></div>
  <div class="field" style="left:601px; top:825px;">Hours<span class="line fixed" style="width:256px;"></span></div>

  <div class="field" style="left:121px; top:896px; width:956px;">Signature<span class="line"></span></div>
  <div class="field" style="left:121px; top:968px; width:956px;">Print<span class="line"></span></div>
</body>
</html>
```